Coffee label for grocery store sales

We need a 3x4 label designed for our expanding grocery store market. I'm looking for something playful that will be eye catching on a shelf. Bag color is negotiable, but would prefer kraft, white, or black.

Target Market(s)

Grocery Stores

Industry/Entity Type

Coffee Shop

Logo Text

Heron Lane Coffee

Colors

Designer to choose colors to be used in the design.

Requirements
Must have
• Space for address label to identify blend.
• 47 W. Oak Ave., Dunmore, WI 54921
• www.heronlanecoffee.example
Nice to have
• Illustrations, bold colors

```html
<!DOCTYPE html>
<html lang="en">
<head>
<meta charset="utf-8">
<title>Heron Lane Coffee – Blend Label</title>
<link rel="stylesheet" href="https://fonts.googleapis.com/css2?family=Special+Elite&family=Courier+Prime:wght@700&display=swap">
<style>
  :root {
    --backdrop: #d9d9db;
    --label-yellow: #e1d868;
    --label-yellow-light: #e8df72;
    --frame-white: #fbfbf3;
    --ink: #1b1b1b;
    --band-white: #f7f7f4;
  }
  * { margin: 0; padding: 0; box-sizing: border-box; }
  html, body {
    width: 1200px;
    height: 800px;
    overflow: hidden;
    background: var(--backdrop);
  }
  .canvas {
    position: relative;
    width: 1200px;
    height: 800px;
    display: flex;
    align-items: center;
    justify-content: center;
  }
  .label {
    position: relative;
    width: 525px;
    height: 700px;
    background: linear-gradient(160deg, var(--label-yellow) 0%, var(--label-yellow-light) 100%);
    color: var(--ink);
  }
  .label__frame {
    position: absolute;
    inset: 12px;
    border: 3px solid var(--frame-white);
  }
  .brand {
    position: absolute;
    top: 58px;
    left: 0;
    width: 100%;
    display: flex;
    justify-content: center;
    align-items: center;
    gap: 14px;
  }
  .brand__bean { width: 34px; height: 50px; }
  .brand__name {
    font-family: "Special Elite", "Courier New", monospace;
    font-size: 24px;
    line-height: 1.05;
    text-align: center;
    color: var(--ink);
  }
  .brew-icons {
    position: absolute;
    top: 172px;
    left: 110px;
    width: 305px;
    height: 110px;
    display: flex;
    justify-content: space-between;
    align-items: flex-end;
  }
  .brew-icons svg { display: block; }
  .blend-band {
    position: absolute;
    top: 295px;
    left: 80px;
    width: 376px;
    height: 86px;
    background: var(--band-white);
    display: flex;
    align-items: center;
    justify-content: center;
  }
  .blend-band__name {
    font-family: "Special Elite", "Courier New", monospace;
    font-size: 40px;
    letter-spacing: 1px;
    color: var(--ink);
  }
  .contact {
    position: absolute;
    top: 462px;
    left: 0;
    width: 100%;
    text-align: center;
    font-family: "Courier Prime", "Courier New", monospace;
    font-weight: 700;
    font-size: 17px;
    line-height: 28px;
    color: var(--ink);
  }
  .cup-mark {
    position: absolute;
    top: 580px;
    left: 50%;
    transform: translateX(-50%);
  }
</style>
</head>
<body>
<main class="canvas">
  <section class="label">
    <div class="label__frame"></div>

    <header class="brand">
      <svg class="brand__bean" viewBox="0 0 34 50" aria-hidden="true">
        <g fill="var(--ink)">
          <ellipse cx="11" cy="33" rx="9" ry="13" transform="rotate(-15 11 33)"/>
          <ellipse cx="24" cy="16" rx="8" ry="12" transform="rotate(20 24 16)"/>
        </g>
        <g fill="none" stroke="var(--label-yellow)" stroke-width="2">
          <path d="M14 21 Q7 33 10 45"/>
          <path d="M20 5 Q28 16 25 27"/>
        </g>
      </svg>
      <p class="brand__name">Heron Lane<br>Coffee</p>
    </header>

    <div class="brew-icons">
      <svg class="icon-cup" width="72" height="60" viewBox="0 0 72 60" aria-label="Cup">
        <path d="M12 6 H56 L52 54 H16 Z" fill="var(--frame-white)" stroke="var(--ink)" stroke-width="4" stroke-linejoin="round"/>
        <path d="M14 6 Q2 8 4 20 Q6 30 16 30" fill="none" stroke="var(--ink)" stroke-width="4"/>
      </svg>
      <svg class="icon-carafe" width="96" height="92" viewBox="0 0 96 92" aria-label="Carafe">
        <path d="M28 4 H62 L66 18 H24 Z" fill="var(--ink)"/>
        <circle cx="44" cy="54" r="34" fill="var(--frame-white)" stroke="var(--ink)" stroke-width="5"/>
        <path d="M14 58 A30 30 0 0 0 74 58 Z" fill="var(--ink)"/>
        <path d="M70 24 H88 V50 L76 62" fill="none" stroke="var(--ink)" stroke-width="6" stroke-linejoin="round"/>
      </svg>
      <svg class="icon-moka" width="76" height="108" viewBox="0 0 76 108" aria-label="Moka pot">
        <path d="M28 2 H44 V10 H28 Z" fill="var(--ink)"/>
        <path d="M16 12 H56 L50 48 H22 Z" fill="var(--ink)"/>
        <path d="M2 20 L16 16 L18 26 Z" fill="var(--ink)"/>
        <path d="M56 18 H70 V42 L56 46" fill="none" stroke="var(--ink)" stroke-width="5"/>
        <rect x="20" y="50" width="32" height="6" fill="var(--ink)"/>
        <path d="M22 58 H50 L58 106 H14 Z" fill="var(--ink)"/>
        <path d="M28 68 H44 L46 94 H26 Z" fill="var(--frame-white)"/>
      </svg>
    </div>

    <div class="blend-band">
      <h1 class="blend-band__name">BLEND NAME</h1>
    </div>

    <address class="contact">
      47 W. Oak Ave., Dunmore, WI 54921<br>
      www.heronlanecoffee.example
    </address>

    <svg class="cup-mark" width="80" height="86" viewBox="0 0 80 86" aria-label="Espresso cup">
      <path d="M28 4 Q22 10 28 16 Q34 22 28 28" fill="none" stroke="var(--ink)" stroke-width="3"/>
      <path d="M36 10 Q32 14 36 18" fill="none" stroke="var(--ink)" stroke-width="3"/>
      <path d="M6 40 H62 L58 70 Q56 82 44 82 H24 Q12 82 10 70 Z" fill="var(--ink)"/>
      <ellipse cx="34" cy="44" rx="24" ry="5" fill="var(--frame-white)"/>
      <path d="M60 48 Q76 48 74 60 Q72 70 56 70" fill="none" stroke="var(--ink)" stroke-width="6"/>
    </svg>
  </section>
</main>
</body>
</html>
```